Flyer für ein Küchenfachgeschäft
Zielgruppe
Wir sind ein Küchenfachgeschäft und würden hierfür gerne einen Flyer für Hochwertige und Qualitative Küchen einen Flyer erstellen lassen.
Aufgabenstellung
US gefaltet Format, Hochwertig und ansprechend. Wir sind Berater, Planer und Ausführer. 35 Jahre Erfahrung

```html
<!DOCTYPE html>
<html lang="de">
<head>
<meta charset="utf-8">
<title>Atelier Kochraum – Flyer</title>
<link href="https://fonts.googleapis.com/css2?family=Oswald:wght@400;500;700&family=Raleway:wght@400;500&display=swap" rel="stylesheet">
<style>
:root{
  --backdrop:#c4c4c4;
  --slate:#555555;
  --gold:#dcc566;
  --ink:#1d1d1d;
  --paper:#ffffff;
  --photo-warm-a:#6e5443;
  --photo-warm-b:#2c2826;
  --photo-dark-a:#3a3d42;
  --photo-dark-b:#151618;
  --photo-room-a:#cdb79a;
  --photo-room-b:#5a4a3c;
}
*{box-sizing:border-box;margin:0;padding:0}
html,body{width:1200px;height:848px;overflow:hidden;background:var(--backdrop)}
body{position:relative;font-family:"Raleway",sans-serif;color:var(--ink)}
.spread{position:absolute;left:307px;width:585px;height:414px;display:grid;grid-template-columns:repeat(3,1fr);box-shadow:0 4px 14px rgba(0,0,0,.25);background:var(--paper)}
.spread--inside{top:8px}
.spread--outside{top:426px}
.panel{position:relative;overflow:hidden}
.panel--slate{background:var(--slate);color:var(--paper)}
.panel--paper{background:var(--paper)}
.photo{position:absolute}
.photo--warm{background:linear-gradient(135deg,var(--photo-warm-a),var(--photo-warm-b))}
.photo--dark{background:linear-gradient(160deg,var(--photo-dark-a),var(--photo-dark-b))}
.photo--room{background:linear-gradient(180deg,#efe9e2 0%,var(--photo-room-a) 45%,var(--photo-room-b) 100%)}
.photo--round{border-radius:50%}
.heading{font-family:"Oswald",sans-serif;font-weight:700;text-transform:uppercase;letter-spacing:-.3px;line-height:1}
.rule{display:block;width:20px;height:4px;background:var(--ink)}
.rule--gold{background:var(--gold)}
.copy{font-size:6.4px;line-height:1.45}
.brands{list-style:none;font-size:6.4px;line-height:1.6;margin-top:7px}
.brands li::before{content:"•";display:inline-block;width:12px;font-size:5px}
/* inside spread */
.intro-circle{left:12px;top:14px;width:112px;height:112px}
.intro-copy{position:absolute;left:60px;top:160px;width:120px}
.side-label{position:absolute;left:-34px;bottom:92px;transform:rotate(-90deg);font-size:22px;color:var(--gold);font-weight:500;white-space:nowrap}
.kochen-title{position:absolute;left:22px;top:36px;font-size:22px}
.kochen-rule{position:absolute;left:36px;top:76px}
.kochen-copy{position:absolute;left:40px;top:86px;width:120px}
.kochen-photo{left:0;right:0;top:220px;bottom:0;clip-path:polygon(0 25%,100% 0,100% 100%,0 100%)}
.wohnen-photo{left:0;right:0;top:0;height:230px}
.wohnen-field{position:absolute;left:0;right:0;top:160px;bottom:0;background:var(--gold);clip-path:polygon(0 0,100% 16%,100% 100%,0 100%);color:var(--paper)}
.wohnen-title{position:absolute;left:30px;top:22px;font-size:20px;font-weight:500;color:var(--paper)}
.wohnen-mark{position:absolute;left:20px;top:62px;width:3px;height:18px;background:var(--paper)}
.wohnen-copy{position:absolute;left:32px;top:60px;width:132px}
/* outside spread */
.cover-photo{left:0;right:0;top:0;height:240px}
.cover-title{position:absolute;left:14px;top:120px;font-size:20px;font-weight:500;color:var(--gold);line-height:1.3}
.cover-field{position:absolute;left:0;right:0;top:180px;bottom:0;background:var(--paper);clip-path:polygon(0 26%,100% 0,100% 100%,0 100%)}
.cover-rule{position:absolute;left:20px;top:254px}
.cover-copy{position:absolute;left:20px;top:270px;width:155px;font-size:10px;line-height:1.55;text-decoration:underline}
.contact-title{position:absolute;left:22px;top:48px;font-family:"Oswald",sans-serif;font-size:22px;color:var(--gold)}
.contact-rule{position:absolute;left:22px;top:88px}
.contact-copy{position:absolute;left:20px;top:105px;width:160px}
.contact-copy p+p{margin-top:6px}
.contact-list{position:absolute;left:34px;top:170px;list-style:none;font-size:6px;line-height:1.65}
.contact-list li{display:flex;align-items:center;gap:5px}
.contact-list svg{width:7px;height:7px;flex:none}
.contact-address{font-family:"Oswald",sans-serif;font-size:5.6px}
.contact-web{position:absolute;left:40px;top:212px;font-family:"Oswald",sans-serif;font-size:5.6px}
.contact-circle{left:34px;top:250px;width:128px;height:128px}
.title-photo{left:10px;right:10px;top:28px;height:178px}
.title-name{position:absolute;left:20px;top:104px;display:flex;align-items:center;gap:6px;font-family:"Raleway",sans-serif;font-weight:500;font-size:16px;color:var(--paper)}
.title-name::before{content:"";width:8px;height:8px;background:var(--paper)}
.title-claim{position:absolute;left:18px;top:232px;font-family:"Oswald",sans-serif;font-weight:500;font-size:21px;letter-spacing:-.4px}
.title-copy{position:absolute;left:18px;top:262px;width:158px;text-align:justify;font-size:6.4px;line-height:1.55}
</style>
</head>
<body>

<section class="spread spread--inside" aria-label="Innenseite">
  <div class="panel panel--slate">
    <div class="photo photo--warm photo--round intro-circle" role="img" aria-label="Foto: Küche mit Holzfronten"></div>
    <div class="intro-copy">
      <p class="copy">Durch unsere langjährige Erfahrung und der aktuellen Technik unseres Mobiliars stehen einer individuellen Planung alle Möglichkeiten offen.</p>
      <ul class="brands"><li>Nordholz Möbel</li><li>Alpenkühl</li><li>Wasserwerk</li><li>Fontana</li><li>Linea</li></ul>
    </div>
    <p class="heading side-label">Feiern |Wohnen</p>
  </div>
  <div class="panel panel--paper">
    <h2 class="heading kochen-title">Kochen</h2>
    <span class="rule kochen-rule"></span>
    <div class="kochen-copy">
      <p class="copy">Ihre Essgewohnheiten, Geschmackswünsche und Kochkenntnisse – abgestimmt mit aktueller Küchentechnik – garantieren Spaß und Freude beim Kochen.</p>
      <ul class="brands"><li>Wohlfühlküchen</li><li>Schweizer präzision</li><li>Individuelle Armaturen</li><li>Italienisches Design</li><li>Rezeptur für Genuss</li></ul>
    </div>
    <div class="photo photo--dark kochen-photo" role="img" aria-label="Foto: dunkle Kücheninsel in hellem Raum"></div>
  </div>
  <div class="panel panel--paper">
    <div class="photo photo--dark wohnen-photo" role="img" aria-label="Foto: Ausstellungsraum mit schwarzer Kücheninsel"></div>
    <div class="wohnen-field">
      <h2 class="heading wohnen-title">Wohnen</h2>
      <span class="wohnen-mark"></span>
      <div class="wohnen-copy">
        <p class="copy">Durch unsere langjährige Erfahrung und der aktuellen Technik unseres Mobiliars stehen einer individuellen Planung alle Möglichkeiten offen.</p>
        <ul class="brands"><li>Nordholz Möbel</li><li>Alpenkühl</li><li>Wasserwerk</li><li>Fontana</li><li>Linea</li></ul>
      </div>
    </div>
  </div>
</section>

<section class="spread spread--outside" aria-label="Außenseite">
  <div class="panel panel--paper">
    <div class="photo photo--dark cover-photo" role="img" aria-label="Foto: schwarze Küche mit Vitrinenschrank"></div>
    <p class="heading cover-title">Kochen | Leben |<br>Feiern |Wohnen</p>
    <div class="cover-field"></div>
    <span class="rule rule--gold cover-rule"></span>
    <p class="cover-copy">Durch unsere langjährige Erfahrung und der aktuellen Technik unseres Mobiliars stehen einer individuellen Planung alle Möglichkeiten offen.</p>
  </div>
  <div class="panel panel--slate">
    <h2 class="contact-title">Kontakt</h2>
    <span class="rule rule--gold contact-rule"></span>
    <div class="contact-copy copy">
      <p>Schön, dass Sie uns gefunden haben und mit uns in Verbindung treten möchten.</p>
      <p>Unser Studio ist donnerstags und freitags von 10 bis 18 Uhr geöffnet. Termine nach Vereinbarung sind möglich.</p>
    </div>
    <ul class="contact-list">
      <li><svg viewBox="0 0 10 10" fill="none" stroke="#fff" stroke-width=".8"><path d="M5 9.5S1.8 6 1.8 3.9a3.2 3.2 0 0 1 6.4 0C8.2 6 5 9.5 5 9.5z"/><circle cx="5" cy="4" r="1.1"/></svg><span class="contact-address">Lindenweg 7 | D-83000 Musterau am See</span></li>
      <li><svg viewBox="0 0 10 10" fill="none" stroke="#fff" stroke-width=".8"><rect x="1" y="2.2" width="8" height="5.6"/><path d="M1 2.2l4 3.2 4-3.2"/></svg>kontakt@atelier-kochraum.example</li>
      <li><svg viewBox="0 0 10 10" fill="none" stroke="#fff" stroke-width=".8"><path d="M2.3 1.2l1.6 1.9-.9 1.2a5 5 0 0 0 2.7 2.7l1.2-.9 1.9 1.6-.9 1.2C5 8.6 1.4 5 1.1 2.1z"/></svg>+49 (0)8000 123450</li>
    </ul>
    <p class="contact-web">www.atelier-kochraum.example</p>
    <div class="photo photo--dark photo--round contact-circle" role="img" aria-label="Foto: schwarze Kücheninsel mit Holzwand"></div>
  </div>
  <div class="panel panel--paper">
    <div class="photo photo--room title-photo" role="img" aria-label="Foto: Ausstellungsraum mit Holzboden und Strahlern"></div>
    <p class="title-name">Atelier Kochraum</p>
    <h1 class="title-claim">Sehen. Hören. Fühlen.</h1>
    <p class="title-copy">Der Besuch im Atelier Kochraum garantiert einen Blick auf neueste Technik. Während Sie uns zuhören verzaubern wir Sie mit unserer Leuchtenwelt. Hochwertigste Materialien, verarbeitet in exklusiven Designs für Outdoor und Indoor erwarten Sie.</p>
  </div>
</section>

</body>
</html>
```